Website Design for recruiting company

We need a homepage mockup for a recruiting company focused on the legal industry. Use your creative talent to come up with something visually appeal and professional for this web-site.

We'd really like to see the maze from the logo incorporated into the design somehow. Please use the website mockup provided as inspiration for this project. We really like the layout and photos!

Target Market(s)

lawyers

Industry/Entity Type

Legal

Number of Pages Required

1 page

Font styles to use
Sans Serif

```html
<!DOCTYPE html>
<html lang="en">
<head>
<meta charset="utf-8">
<title>Harbor Counsel Search — Legal Recruiting</title>
<link href="https://fonts.googleapis.com/css2?family=Poppins:wght@700;800&family=Roboto:wght@400;500;700&display=swap" rel="stylesheet">
<style>
:root{
  --plum:#756673;
  --plum-dark:#5f525d;
  --ink:#111111;
  --text:#4a4548;
  --muted:#7b767a;
  --sage:#c4cab8;
  --sage-bg:#dde0d6;
  --paper:#efefea;
  --white:#ffffff;
  --line:#dcdcdc;
}
*{margin:0;padding:0;box-sizing:border-box}
html,body{width:1200px;height:3646px;overflow:hidden;background:var(--white)}
body{position:relative;font-family:"Roboto",Arial,sans-serif;color:var(--text)}
.abs{position:absolute}
.btn{position:absolute;display:flex;align-items:center;justify-content:center;background:var(--plum);color:var(--white);font:500 17px "Roboto",sans-serif;border-radius:4px;letter-spacing:.2px;text-decoration:none}
.btn.sage{background:var(--sage)}
.photo{position:absolute}

.hero{position:absolute;left:0;top:0;width:1200px;height:676px;background:var(--paper)}
.brand{position:absolute;left:79px;top:14px;display:flex;align-items:center;gap:14px}
.brand-mark{width:68px;height:68px;border-radius:50%;background:var(--plum);opacity:.85}
.brand-name{font:400 13px "Roboto",sans-serif;color:var(--muted)}
.nav{position:absolute;top:38px;font:400 16px "Roboto",sans-serif;color:var(--text);white-space:nowrap}
.nav.active{color:var(--muted)}
.nav.active::before{content:"";position:absolute;left:-13px;top:7px;width:7px;height:7px;border-radius:50%;background:#9a969a}
.phone{position:absolute;left:974px;top:29px;display:flex;align-items:center;gap:10px;font:500 16px "Roboto",sans-serif;color:var(--text)}

.hero-title{position:absolute;left:147px;top:238px;font:800 42px/52px "Poppins",sans-serif;color:var(--plum);letter-spacing:.5px}
.hero-title b{color:var(--ink);font-weight:800}
.hero-sub{position:absolute;left:151px;top:406px;font:400 20px "Roboto",sans-serif;color:var(--ink)}

.finder{position:absolute;left:132px;top:630px;width:936px;height:103px;background:var(--white);border-radius:4px;box-shadow:0 3px 14px rgba(0,0,0,.1)}
.finder h2{position:absolute;left:31px;top:36px;font:700 22px "Roboto",sans-serif;color:var(--plum)}
.field{position:absolute;height:46px;border:1px solid var(--line);font:400 14px "Roboto",sans-serif;color:#9a9a9a;display:flex;align-items:center;padding-left:18px;background:var(--white)}

.about-h{position:absolute;left:637px;top:806px;font:500 44px "Roboto",sans-serif;color:var(--plum)}
.about-sub{position:absolute;left:640px;top:862px;font:400 15px "Roboto",sans-serif;color:var(--ink)}
.about-p{position:absolute;left:641px;width:420px;font:400 14.5px/27px "Roboto",sans-serif;color:var(--text);white-space:nowrap}

.emp-band{position:absolute;left:0;top:1348px;width:600px;height:385px;background:var(--sage-bg)}
.emp-h{position:absolute;left:76px;top:1426px;font:500 40px "Roboto",sans-serif;color:var(--plum)}
.emp-p{position:absolute;left:78px;top:1492px;width:460px;font:400 15px/27px "Roboto",sans-serif;color:var(--text);white-space:nowrap}

.sec-h{position:absolute;left:0;width:1200px;text-align:center;font:500 42px "Roboto",sans-serif;color:var(--plum)}
.sec-sub{position:absolute;left:0;width:1200px;text-align:center;font:400 15px/23px "Roboto",sans-serif;color:var(--text)}
.job{position:absolute;left:246px;width:709px;height:105px;background:var(--white);box-shadow:0 2px 10px rgba(0,0,0,.08)}
.job .thumb{position:absolute;left:0;top:0;width:128px;height:105px;border-radius:3px 0 0 3px}
.job .title{position:absolute;left:157px;top:28px;font:500 20px "Roboto",sans-serif;color:var(--plum)}
.job .loc{position:absolute;left:157px;top:57px;font:400 16px "Roboto",sans-serif;color:var(--ink);letter-spacing:.4px}
.job .desc{position:absolute;left:323px;top:30px;width:240px;font:400 14px/23px "Roboto",sans-serif;color:var(--text);white-space:nowrap}
.job .btn{left:607px;top:29px;width:84px;height:46px;font-size:15px}

.talent{position:absolute;left:0;top:2734px;width:1200px;height:581px;background:var(--paper)}

.foot-mark{position:absolute;left:549px;top:3366px;width:102px;height:102px;border-radius:50%;background:var(--plum);opacity:.85}
.social{position:absolute;top:3485px;width:42px;height:42px;border-radius:50%;background:var(--plum)}
.foot-t{position:absolute;left:0;width:1200px;text-align:center;font:400 14px "Roboto",sans-serif;color:var(--text)}
</style>
</head>
<body>

<header class="hero">
  <div class="brand">
    <div class="brand-mark"></div>
    <span class="brand-name">Harbor Counsel Search</span>
  </div>
  <nav>
    <span class="nav active" style="left:474px">Home</span>
    <span class="nav" style="left:540px">About Us</span>
    <span class="nav" style="left:629px">Whats's New</span>
    <span class="nav" style="left:749px">For Employers</span>
    <span class="nav" style="left:869px">Contact Us</span>
  </nav>
  <div class="phone">
    <svg width="38" height="38" viewBox="0 0 38 38" aria-hidden="true">
      <circle cx="19" cy="19" r="17.5" fill="none" stroke="#7b767a" stroke-width="1.5"/>
      <path d="M13 12c1-1 2-1 3 0l2 3c.5 1 0 2-1 2.5 1 2 2.5 3.5 4.5 4.5.5-1 1.5-1.5 2.5-1l3 2c1 1 1 2 0 3-2 2-5 1.5-8.5-1.5S11 15 13 12z" fill="#7b767a"/>
    </svg>
    <span>555 014 2290</span>
  </div>

  <div class="abs" style="left:928px;top:194px;width:122px;height:120px;border-radius:50%;background:#dfe4d5"></div>
  <div class="abs" style="left:565px;top:410px;width:150px;height:130px;border-radius:50%;background:#e1e5d8"></div>
  <div class="abs" style="left:980px;top:430px;width:155px;height:130px;border-radius:50%;background:#e1e5d8"></div>
  <div class="photo" role="img" aria-label="Smiling young lawyer in a dark suit and tie, arms crossed" style="left:637px;top:156px;width:390px;height:474px;background:linear-gradient(180deg,#c9b39f 0%,#8a7465 30%,#2f2f36 60%,#242429 100%);border-radius:120px 120px 0 0"></div>

  <h1 class="hero-title">START HERE,<br>LET OUR <b>EXPERIENCE</b><br>GUIDE YOU</h1>
  <p class="hero-sub">Harbor Counsel Search</p>
  <a class="btn" style="left:154px;top:443px;width:167px;height:52px">SEARCH JOB</a>
</header>

<section class="finder">
  <h2>Find Your Perfect Job.</h2>
  <div class="field" style="left:285px;top:29px;width:240px">Job Title or Keyword</div>
  <div class="field" style="left:533px;top:29px;width:238px">City, State , Zip</div>
  <a class="btn" style="left:779px;top:29px;width:136px;height:46px;font-size:16px">SEARCH JOB</a>
</section>

<section>
  <div class="abs" style="left:171px;top:877px;width:245px;height:336px;background:var(--plum)"></div>
  <div class="photo" role="img" aria-label="Colleagues smiling in a meeting around a laptop" style="left:204px;top:799px;width:373px;height:391px;background:linear-gradient(135deg,#d8d6d0 0%,#b8b2a8 45%,#6a707a 75%,#2f3e55 100%)"></div>
  <h2 class="about-h">About Us</h2>
  <p class="about-sub">Harbor Counsel Search</p>
  <p class="about-p" style="top:904px">Harbor Counsel Search focuses on the permanent<br>placement of attorneys withlaw firms and corporations in<br>the New England area.</p>
  <p class="about-p" style="top:995px">Founded in 1982, Harbor Counsel Search is the oldest<br>attorney search firm in New England, and isranked the<br>number one legal recruiter in New England in the most<br>recent surveyconducted by The Counsel Review</p>
  <a class="btn" style="left:641px;top:1116px;width:166px;height:51px">LEARN MORE</a>
</section>

<section>
  <div class="emp-band"></div>
  <div class="photo" role="img" aria-label="Smiling candidate shaking hands with an interviewer at an office desk" style="left:600px;top:1295px;width:600px;height:499px;background:linear-gradient(120deg,#8b7f76 0%,#b79a87 35%,#d5d1c9 60%,#9fb1c4 100%)"></div>
  <h2 class="emp-h">For Employers</h2>
  <p class="emp-p">Our unparalleled recruiting industry and legal experience<br>have generated anextensive network of contacts<br>throughout the legal community.</p>
  <div class="field" style="left:76px;top:1595px;width:330px;height:51px;border:none">Find The Right Candidate</div>
  <a class="btn" style="left:406px;top:1595px;width:156px;height:51px;border-radius:0 4px 4px 0">START HERE</a>
</section>

<section>
  <h2 class="sec-h" style="top:1852px">Whats's New</h2>
  <p class="sec-sub" style="top:1911px">Below are our most recent listings. All positions are in the greater<br>Boston area unless otherwise noted.</p>

  <article class="job" style="top:1989px">
    <div class="thumb" role="img" aria-label="Waterfront hotel at dusk" style="background:linear-gradient(180deg,#6c7fb0,#b9a890 60%,#4a4440)"></div>
    <div class="title">Job Title</div><div class="loc">New england</div>
    <p class="desc">Lorem Ipsum is simply dummy<br>text of the printing &amp; type.</p>
    <a class="btn">MORE</a>
  </article>
  <article class="job" style="top:2114px">
    <div class="thumb" role="img" aria-label="Team meeting at a table" style="background:linear-gradient(135deg,#5a5d63,#9a958e,#3d4148)"></div>
    <div class="title">Job Title</div><div class="loc">New england</div>
    <p class="desc">Lorem Ipsum is simply dummy<br>text of the printing &amp; type.</p>
    <a class="btn sage">MORE</a>
  </article>
  <article class="job" style="top:2238px">
    <div class="thumb" role="img" aria-label="Professionals in an office" style="background:linear-gradient(135deg,#3f444c,#7b7a78,#2e3136)"></div>
    <div class="title">Job Title</div><div class="loc">New england</div>
    <p class="desc">Lorem Ipsum is simply dummy<br>text of the printing &amp; type.</p>
    <a class="btn sage">MORE</a>
  </article>
  <article class="job" style="top:2363px">
    <div class="thumb" role="img" aria-label="Two colleagues reviewing documents" style="background:linear-gradient(135deg,#4a4c50,#8c8883,#3a3b3e)"></div>
    <div class="title">Job Title</div><div class="loc">New england</div>
    <p class="desc">Lorem Ipsum is simply dummy<br>text of the printing &amp; type.</p>
    <a class="btn sage">MORE</a>
  </article>
  <article class="job" style="top:2487px">
    <div class="thumb" role="img" aria-label="Business people shaking hands" style="background:linear-gradient(135deg,#36393e,#77736e,#2b2d31)"></div>
    <div class="title">Job Title</div><div class="loc">New england</div>
    <p class="desc">Lorem Ipsum is simply dummy<br>text of the printing &amp; type.</p>
    <a class="btn sage">MORE</a>
  </article>

  <a class="btn" style="left:517px;top:2619px;width:166px;height:51px">SEARCH JOB</a>
</section>

<section class="talent">
  <h2 class="sec-h" style="top:70px;font-size:39px">Delivering the Talent Your Business Needs.</h2>
  <p class="sec-sub" style="top:120px;font-size:16px;color:var(--ink);letter-spacing:.4px">Harbor Counsel Search</p>
  <a class="btn" style="left:498px;top:163px;width:204px;height:51px">REQUEST TALENT</a>
  <div class="photo" role="img" aria-label="Group of diverse smiling legal professionals in business attire" style="left:0;top:259px;width:1200px;height:322px;background:linear-gradient(180deg,#efefea 0%,#c9b2a0 30%,#5d5d66 65%,#2f3038 100%)"></div>
</section>

<footer>
  <div class="foot-mark"></div>
  <a class="social" style="left:532px" aria-label="Social profile one"></a>
  <a class="social" style="left:580px" aria-label="Social profile two"></a>
  <a class="social" style="left:626px" aria-label="Social profile three"></a>
  <p class="foot-t" style="top:3545px">info@harborcounsel.example</p>
  <p class="foot-t" style="top:3574px">©Lantern Studio -2020 All rights reserved.</p>
</footer>

</body>
</html>
```